Mosswood Chiropractic Web Design

We need a fully operating Web site design INCLUDING the code for a Chiropractic Clinic based in Auckland New Zealand to target people from different financial backgrounds.

We need 4 Pages as followed:
1. Home: includes Slideshow of the clinic, General information about chiropractic, option for "Request an appointment", and it would be nice to have a picture on the top right side of the header and the clinic's name and logo on the top left side. on the bottom right we would like a small section for "Testimonial" (A good example: http://www.fernlightstudio.example/ )
(A good example for slide show is: http://www.bektora.example.nz/)
(A good example for the header is: http://www.spinewellpraxis.example/)

2. About Us: this section will include the background information of the company, and a section for our staff (which will includes a photo and description of each person/staff which can be changedanytime)
(a good example: http://www.harbourlanechiro.example.nz/)

3. Contact: includes location, map, contact numbers, email, and a contact box (A good example: http://www.fernlightstudio.example/contact/)

4. Services: includes our products, adjustment equipment, chiropractic products for sale, few pictures of patients while under chiropractic care/adjustment tables

We would also like to add "social networking" options on the bottom left side of every page (Facebook, twitter, Blog, Google+)

Please check the following links to get a feel of our favorite designs:
http://www.spinewellpraxis.example/
http://www.harbourlanechiro.example.nz/
http://www.bektora.example.nz/
http://www.brindlechiropracticclinic.example/
http://www.stillwoven.example.nz/
http://www.pqr.example.nz/index-1.html
http://home.keelbrookchiro.example.nz/home/

we would like to have full access to the back-end- admin of the website to be able to change and add any pictures or texts.
Updates

Hi Lovely Designer,

thank you so much for your proposed designs. We just uploaded the original source file of our logo, for you all to have access on it to facilitate your work. 

Enjoy your day

Orla

Target Market(s)

People with different financial background as well as we are located in the artistic part of town, so appealing to those crowd is important to us.

Industry/Entity Type

Financial

Requirements
Must have
• 1.color similar to the logo or darker colors (Dark and rich colors are prefered)
2. more artistic than a basic doctors' clinic
3. I would like the opening of the web to bring art, tranquility and peaceful images into mind
Should not have
• Not bombarded with lots of info and pics in one page, not too busy and crowded

```html
<!DOCTYPE html>
<html lang="en">
<head>
<meta charset="utf-8">
<title>Mosswood Chiropractic</title>
<link href="https://fonts.googleapis.com/css2?family=Open+Sans:ital,wght@0,300;0,400;0,600;0,700;1,400&display=swap" rel="stylesheet">
<style>
:root{
  --navy:#0f2f57;
  --navy-deep:#0a2444;
  --green:#a8c97b;
  --green-dark:#8fb35e;
  --teal:#3ba3c3;
  --band:#4196ad;
  --ink:#333;
  --muted:#666;
  --line:#c9d3de;
  --icon:#a7b6c8;
  --panel:#e4e4e4;
  --footer:#2b2e30;
  --footer-bar:#1e2021;
  --footer-text:#9a9ea1;
  --accent:#e0522a;
  --white:#fff;
}
*{box-sizing:border-box;margin:0;padding:0}
html,body{width:1200px;height:2617px;overflow:hidden;background:var(--white)}
body{position:relative;font-family:"Open Sans",Arial,sans-serif;color:var(--ink)}
.abs{position:absolute}

/* header */
.brand{left:73px;top:35px;width:329px;height:87px;background:linear-gradient(#1c4779,var(--navy));display:flex;align-items:center;gap:12px;padding-left:20px}
.brand-dot{flex:none;width:22px;height:22px;border-radius:50%;background:#8fb0d3}
.brand-name{color:#dfe9f4;font-size:23px;font-weight:400;line-height:1;white-space:nowrap}
.social{top:33px;width:50px;height:50px;border:2px solid #dde2e7;border-radius:50%}
.phone-pill{left:961px;top:33px;width:177px;height:50px;border:2px solid #dde2e7;border-radius:25px;display:flex;align-items:center;gap:10px;padding-left:18px;color:#b4bcc4;font-size:16px;white-space:nowrap}
.nav{left:60px;top:122px;width:1078px;height:39px;background:var(--navy-deep);display:flex}
.nav a{color:var(--white);text-decoration:none;font-size:14px;font-weight:600;padding:0 22px;line-height:39px;border-right:1px solid #244672}
.search{left:908px;top:127px;width:223px;height:29px;background:var(--green);color:#d4e6b9;font-size:13px;padding-left:12px;line-height:29px}
.hero{left:60px;top:161px;width:1078px;height:502px;background:linear-gradient(180deg,#f6f6f6 0%,#e4e4e4 55%,#d8d4d2 100%)}
.features{left:60px;top:663px;width:1078px;height:80px;background:var(--green);display:flex;padding:16px 0 0 20px}
.features div{width:216px;color:var(--white);font-size:13px;line-height:1.55}
.features b{display:block;font-size:15px;font-weight:700}

/* services */
.tagline{top:785px;left:0;width:1200px;text-align:center;font-size:35px;font-weight:300;color:var(--navy)}
.service{top:872px;width:240px;text-align:center}
.service .ring{width:122px;height:122px;margin:0 auto;border:3px solid var(--line);border-radius:50%;display:flex;align-items:center;justify-content:center}
.service h3{margin-top:30px;font-size:19px;font-weight:600;color:#333}
.service p{margin-top:10px;font-size:14px;line-height:1.6;color:var(--muted)}
.rule{left:60px;top:1162px;width:1078px;height:1px;background:#e6e6e6}

/* staff */
.section-title{font-size:36px;font-weight:300;color:var(--teal)}
.lead{font-size:14px;color:var(--muted)}
.lead em{color:var(--accent);font-style:normal}
.staff{top:1325px;width:215px}
.staff h4{font-size:17px;font-weight:700;color:#222;white-space:nowrap}
.staff .photo{margin-top:14px;width:215px;height:170px;border:4px solid #dde0e3;background:linear-gradient(160deg,#eef1f4,#d6c2b4 55%,#b7a89a);position:relative}
.staff .role{position:absolute;right:0;bottom:0;background:#6e7377;color:var(--white);font-size:13px;padding:4px 10px}
.staff p{margin-top:26px;font-size:14px;line-height:1.6;color:var(--muted)}

/* appointment */
.appt{left:800px;top:1231px;width:340px;height:636px;background:var(--panel)}
.appt-head{height:121px;background:linear-gradient(#1c4779,var(--navy-deep));padding:16px 27px;color:var(--white)}
.appt-head h2{font-size:27px;font-weight:400}
.appt-head .num{margin-top:10px;display:flex;align-items:center;gap:14px;font-size:29px;font-weight:600;white-space:nowrap}
.appt-head .num span{width:36px;height:36px;border-radius:50%;background:#5b88b5;display:flex;align-items:center;justify-content:center}
.or{left:950px;top:1331px;width:38px;height:38px;border-radius:50%;background:var(--accent);color:var(--white);font-size:13px;font-weight:700;text-align:center;line-height:38px}
.field{left:835px;width:270px;height:35px;background:var(--white);border:1px solid #d4d4d4;font-size:13px;color:#999;padding:8px 10px}
.captcha{left:835px;top:1737px;width:115px;height:38px;background:#f2f2f2;color:var(--accent);font-size:24px;padding-left:10px;line-height:38px;letter-spacing:1px}
.captcha-in{left:958px;top:1737px;width:73px;height:38px;background:var(--white);border:1px solid #d4d4d4}
.submit{left:835px;top:1797px;width:140px;height:35px;background:var(--green-dark);color:var(--white);font-size:13px;font-weight:600;text-align:center;line-height:35px}

/* testimonial */
.avatar{left:58px;top:1832px;width:92px;height:92px;border-radius:50%;border:3px solid #dde0e3;background:linear-gradient(#cfe0f0,#c9b19c)}
.quote{left:172px;top:1830px;width:580px;font-size:17px;font-style:italic;line-height:1.55;color:#555}
.author{left:60px;top:1984px;font-size:14px;color:#555}
.author span{color:var(--accent)}
.arrow{top:2010px;width:20px;height:20px;background:#ccc;border-radius:2px}

/* twitter band */
.band{left:60px;top:2099px;width:1080px;height:69px;background:linear-gradient(#4ea3ba,var(--band));display:flex;align-items:center;padding-left:28px;gap:40px;color:var(--white);font-size:14px;font-weight:600}
.band .bird{width:40px;height:40px;border-radius:50%;background:#2e7f96}
.band a{color:var(--white)}

/* footer */
.footer{left:0;top:2168px;width:1200px;height:395px;background:var(--footer)}
.footer-col{top:2230px;color:var(--footer-text);font-size:14px;line-height:1.7}
.footer-col h5{font-size:27px;font-weight:300;color:var(--white);margin-bottom:18px}
.footer-col b{color:#c8cbcd;font-weight:600}
.news{left:893px;top:2292px;width:307px;height:126px;background:#e2e2e2;padding:20px 20px;font-size:14px;color:#666;white-space:nowrap;overflow:hidden}
.news .in{margin-top:14px;display:flex;gap:14px}
.news .in div:first-child{width:184px;height:38px;background:var(--white);border:1px solid #ccc;padding:8px 10px;font-size:13px;color:#999}
.news .go{width:44px;height:38px;background:var(--green-dark);border-radius:3px}
.footer-rule{left:617px;top:2383px;width:243px;height:1px;background:#666}
.footer-bar{left:0;top:2563px;width:1200px;height:54px;background:var(--footer-bar);color:#aaa;font-size:13px;padding-left:60px;line-height:54px}
</style>
</head>
<body>

<header>
  <div class="abs brand"><span class="brand-dot"></span><span class="brand-name">Mosswood Chiropractic</span></div>
  <div class="abs social" style="left:787px"></div>
  <div class="abs social" style="left:844px"></div>
  <div class="abs social" style="left:902px"></div>
  <div class="abs phone-pill">
    <svg width="14" height="20" viewBox="0 0 14 20"><rect x="1" y="1" width="12" height="18" rx="2" fill="none" stroke="#b4bcc4" stroke-width="2"/><rect x="4" y="4" width="6" height="7" fill="#b4bcc4"/></svg>
    1.800.555.0142
  </div>
  <nav class="abs nav"><a href="#">Home</a><a href="#">About us</a><a href="#">Services</a><a href="#">Contact Us</a></nav>
  <div class="abs search">Search</div>
  <div class="abs hero" role="img" aria-label="Slideshow photograph of a patient with lower back pain"></div>
  <div class="abs features">
    <div><b>Chiropractic</b>Safe and effective</div>
    <div><b>Chiropractors</b>Are medically trained</div>
    <div><b>Using</b>Safe manual adjustments</div>
    <div><b>Restore mobility</b>And relieve pain</div>
    <div><b>Our treatment</b>Manipulation technique</div>
  </div>
</header>

<main>
  <h1 class="abs tagline">We treat all joint, muscle and nerve pain</h1>

  <div class="abs service" style="left:48px">
    <div class="ring"><svg width="56" height="50" viewBox="0 0 56 50"><path d="M18 2l10 10 10-10" fill="none" stroke="#a7b6c8" stroke-width="3"/><rect x="3" y="12" width="50" height="34" rx="3" fill="none" stroke="#a7b6c8" stroke-width="3"/><rect x="10" y="18" width="28" height="22" fill="#a7b6c8"/><circle cx="45" cy="22" r="3" fill="#a7b6c8"/><circle cx="45" cy="32" r="3" fill="#a7b6c8"/></svg></div>
    <h3>Treatments</h3><p>Lorem ipsum dolor sit amet,<br>consectetuer adipiscing elit.</p>
  </div>
  <div class="abs service" style="left:265px">
    <div class="ring"><svg width="60" height="36" viewBox="0 0 60 36"><path d="M3 18C15 2 45 2 57 18 45 34 15 34 3 18z" fill="none" stroke="#a7b6c8" stroke-width="3"/><circle cx="30" cy="18" r="9" fill="#a7b6c8"/></svg></div>
    <h3>Chiropractic Advice</h3><p>Lorem ipsum dolor sit amet,<br>consectetuer adipiscing elit.</p>
  </div>
  <div class="abs service" style="left:481px">
    <div class="ring"><svg width="56" height="56" viewBox="0 0 56 56"><rect x="14" y="4" width="28" height="12" rx="3" fill="#a7b6c8"/><rect x="12" y="22" width="32" height="12" rx="3" fill="#a7b6c8"/><rect x="14" y="40" width="28" height="12" rx="3" fill="#a7b6c8"/><rect x="4" y="24" width="8" height="8" fill="#a7b6c8"/><rect x="44" y="24" width="8" height="8" fill="#a7b6c8"/></svg></div>
    <h3>Chiropractic Glossary</h3><p>Lorem ipsum dolor sit amet,<br>consectetuer adipiscing elit.</p>
  </div>
  <div class="abs service" style="left:698px">
    <div class="ring"><svg width="54" height="46" viewBox="0 0 54 46"><path d="M19 10V4h16v6" fill="none" stroke="#a7b6c8" stroke-width="3"/><rect x="2" y="10" width="50" height="34" rx="4" fill="#a7b6c8"/><path d="M27 17v20M17 27h20" stroke="#fff" stroke-width="6"/></svg></div>
    <h3>Chiropractic History</h3><p>Lorem ipsum dolor sit amet,<br>consectetuer adipiscing elit.</p>
  </div>
  <div class="abs service" style="left:912px">
    <div class="ring"><svg width="48" height="48" viewBox="0 0 48 48"><path d="M10 4l8 10-5 5c3 7 9 13 16 16l5-5 10 8-6 7C20 43 5 28 3 10z" fill="none" stroke="#a7b6c8" stroke-width="3" stroke-linejoin="round"/></svg></div>
    <h3>Contact us</h3><p>Lorem ipsum dolor sit amet,<br>consectetuer adipiscing elit.</p>
  </div>

  <div class="abs rule"></div>

  <h2 class="abs section-title" style="left:60px;top:1226px">Meet our staff</h2>
  <p class="abs lead" style="left:60px;top:1276px">Lorem ipsum dolor sit amet, consectetuer adipiscing elit, sed diam <em>nonummy</em></p>

  <div class="abs staff" style="left:60px">
    <h4>Dr.Mirela Tanvick</h4>
    <div class="photo" role="img" aria-label="Portrait photo of the chiropractor"><span class="role">Chiropractic</span></div>
    <p>Harbourview General Hospital – Sydney June 2009 to July 2010 Lorem ipsum dolor sit amet, consectetur adipiscing...</p>
  </div>
  <div class="abs staff" style="left:307px">
    <h4>Dr.Serafine Holt</h4>
    <div class="photo" role="img" aria-label="Portrait photo of the physiotherapist"><span class="role">Physio</span></div>
    <p>Harbourview General Hospital – Sydney June 2009 to July 2010 Lorem ipsum dolor sit amet, consectetur adipiscing...</p>
  </div>
  <div class="abs staff" style="left:555px">
    <h4>Dr.Ivana Brookwell</h4>
    <div class="photo" role="img" aria-label="Portrait photo of the chiropractor"><span class="role">Chiropractic</span></div>
    <p>Harbourview General Hospital – Sydney June 2009 to July 2010 Lorem ipsum dolor sit amet, consectetur adipiscing...</p>
  </div>

  <aside class="abs appt">
    <div class="appt-head">
      <h2>Make an Appointment</h2>
      <div class="num"><span><svg width="14" height="20" viewBox="0 0 14 20"><rect x="1" y="1" width="12" height="18" rx="2" fill="none" stroke="#fff" stroke-width="2"/><rect x="4" y="4" width="6" height="7" fill="#fff"/></svg></span>1-800-555-0142</div>
    </div>
  </aside>
  <div class="abs or">OR</div>
  <div class="abs field" style="top:1383px">Full Name</div>
  <div class="abs field" style="top:1436px">Phone Number</div>
  <div class="abs field" style="top:1490px">Email Address</div>
  <div class="abs field" style="top:1543px">Appointment Date</div>
  <div class="abs field" style="top:1600px;height:108px">Message</div>
  <div class="abs captcha">oiybi</div>
  <div class="abs captcha-in"></div>
  <div class="abs submit">Submit Request</div>

  <h2 class="abs section-title" style="left:60px;top:1745px">What our patients say</h2>
  <div class="abs avatar" role="img" aria-label="Photo of the patient giving the testimonial"></div>
  <p class="abs quote">Nam liber tempor cum soluta nobis eleifend option congue nihil imperdiet doming id quod mazim placerat facer possim assum. Typi non habent claritatem insitam; est usus legentis in iis qui facit eorum claritatem. Investigationes demonstraverunt lectores legere me lius quod ii legunt saepius.</p>
  <p class="abs author"><span>Owen Ratcliffe</span>, ENT Department</p>
  <div class="abs arrow" style="left:168px"><svg width="20" height="20"><path d="M12 5l-5 5 5 5" fill="none" stroke="#fff" stroke-width="2"/></svg></div>
  <div class="abs arrow" style="left:194px"><svg width="20" height="20"><path d="M8 5l5 5-5 5" fill="none" stroke="#fff" stroke-width="2"/></svg></div>

  <div class="abs band"><span class="bird"></span><span>Freebie Friday: Free Marketplace Files for June <a href="#">mswd.example/126TCW</a></span></div>
</main>

<footer>
  <div class="abs footer"></div>
  <div class="abs footer-col" style="left:60px;top:2232px;width:230px;font-size:13px">Lorem ipsum dolor sit amet, consectetur adipiscing elit. Duis adipiscing id nulla vel lorem dapibus fringilla eget non felis, porttitor lectus.</div>
  <div class="abs footer-col" style="left:338px;width:240px">
    <h5>Location</h5>
    <p>Address will be appear here, some details here City Name, Stat &amp; Country.</p>
    <p style="margin-top:16px"><b>Ph:</b> +800 555 0142</p>
    <p style="margin-top:16px"><b>Email:</b> info@mosswood.example</p>
  </div>
  <div class="abs footer-col" style="left:617px;width:250px">
    <h5>Quick Contact</h5>
    <p><b>Work :</b> +64 - 555 - 010 - 2290</p>
    <p><b>Cell :</b> +64 - 5550102291</p>
    <p><b>Fax :</b> +64 - 555 - 010 - 2292</p>
  </div>
  <div class="abs footer-rule"></div>
  <div class="abs footer-col" style="left:893px"><h5>Newsletter</h5></div>
  <div class="abs news">
    Sign up our newsletter to get latest updates
    <div class="in"><div>Email Address</div><div class="go"></div></div>
  </div>
  <div class="abs footer-bar">© 2013 Mosswood Chiropractic</div>
</footer>

</body>
</html>
```